Quorvex clinic business card - double sided for young clinic

I require business cards for my aesthetic clinic specialising in the below treatments. I would like the cards to be modern as my clinic base are young 22-35 years old. I require my logo on it and would like the edges to be rounded.

I have an aesthetic clinic specialising in :
Quorvex
Lip Enhancement
Chemical Peels
Facial Fillers
Non Surgical Face Lift

I would the cards to have the following information on them:
My logo - (in grey/silver)
address
Phone number
services

Colours :
White/grey/silver and red

a nice image on there, perhaps a set of lips as this is a main service i deliver

Company Name: PDA Address: 52 Farrowmere Road, 4 Brackwell High Street, KT9 4WQ Phone: 0208 794 2160 Website: www.penningtondoweaesthetics.co.uk

Target Market(s)

clinics 22-45 years old mainly female

Industry/Entity Type

Business

Contact Information for Business Card

as above

Requirements
Must have
• logo
• Address
• Email
• Phone number
• Services i offer
Nice to have
• images

```html
<!DOCTYPE html>
<html lang="en">
<head>
<meta charset="utf-8">
<title>PDA – Business Card, Front and Back</title>
<link rel="stylesheet" href="https://fonts.googleapis.com/css2?family=Roboto+Slab:wght@400&family=Arimo:wght@400;700&display=swap">
<style>
  :root {
    --page: #e9e9ea;
    --card-white: #ffffff;
    --silver: #a7a8aa;
    --silver-dark: #8e8f92;
    --ink: #2b2b2b;
    --on-grey: #ffffff;
    --radius: 18px;
  }
  * { box-sizing: border-box; margin: 0; padding: 0; }
  html, body { width: 1200px; height: 950px; overflow: hidden; }
  body {
    background: var(--page);
    font-family: "Arimo", Arial, sans-serif;
    position: relative;
  }
  .card {
    position: absolute;
    left: 250px;
    width: 700px;
    height: 390px;
    border-radius: var(--radius);
    overflow: hidden;
    background: var(--card-white);
    box-shadow: 0 6px 18px rgba(0,0,0,0.12);
  }
  .card--front { top: 70px; }
  .card--back { top: 490px; }

  /* Front */
  .brand {
    position: absolute;
    left: 60px;
    top: 125px;
    display: flex;
    align-items: center;
    gap: 22px;
  }
  .brand__dot {
    width: 86px; height: 86px;
    border-radius: 50%;
    background: var(--silver);
    flex: none;
  }
  .brand__name {
    font-family: "Roboto Slab", Georgia, serif;
    font-weight: 400;
    color: var(--silver);
    text-transform: uppercase;
    line-height: 1.05;
  }
  .brand__name .line1 { display: block; font-size: 21px; letter-spacing: 4px; }
  .brand__name .line2 { display: block; font-size: 34px; letter-spacing: 3px; }

  .services {
    position: absolute;
    left: 430px;
    top: 120px;
    color: var(--ink);
  }
  .services__title { font-size: 19px; font-weight: 700; margin-bottom: 8px; }
  .services__list { list-style: none; font-size: 16px; line-height: 1.55; }
  .services__list li::before { content: "\2022"; margin-right: 8px; }

  /* Back */
  .back__panel {
    position: absolute;
    left: 0; top: 0;
    width: 400px; height: 100%;
    background: var(--silver);
  }
  .contact {
    position: absolute;
    left: 42px;
    top: 48px;
    color: var(--on-grey);
  }
  .contact__name { font-size: 22px; font-weight: 700; }
  .contact__role { font-size: 16px; margin-bottom: 18px; }
  .contact__row {
    display: flex; align-items: center; gap: 10px;
    font-size: 16px; line-height: 1.6;
  }
  .contact__row svg { width: 16px; height: 16px; flex: none; }
  .contact__address { font-size: 16px; line-height: 1.45; margin-top: 10px; }

  .wordmark-vertical {
    position: absolute;
    right: 40px;
    top: 50%;
    transform: translate(50%, -50%) rotate(-90deg) translateY(-50%);
    transform-origin: center;
    font-family: "Roboto Slab", Georgia, serif;
    font-weight: 400;
    color: var(--silver);
    text-transform: uppercase;
    line-height: 1.05;
    white-space: nowrap;
  }
  .wordmark-vertical .line1 { display: block; font-size: 21px; letter-spacing: 4px; }
  .wordmark-vertical .line2 { display: block; font-size: 34px; letter-spacing: 3px; }
</style>
</head>
<body>

<section class="card card--front" aria-label="Business card front">
  <div class="brand">
    <span class="brand__dot" aria-hidden="true"></span>
    <p class="brand__name">
      <span class="line1">Pennington Dowe</span>
      <span class="line2">Aesthetics</span>
    </p>
  </div>
  <div class="services">
    <h2 class="services__title">Specialising in</h2>
    <ul class="services__list">
      <li>Quorvex</li>
      <li>Lip Enhancement</li>
      <li>Chemical Peels</li>
      <li>Facial Fillers</li>
      <li>Non Surgical Face Lift</li>
    </ul>
  </div>
</section>

<section class="card card--back" aria-label="Business card back">
  <div class="back__panel"></div>
  <div class="contact">
    <p class="contact__name">Mara Ellison</p>
    <p class="contact__role">President</p>
    <p class="contact__row">
      <svg viewBox="0 0 16 16" aria-hidden="true"><path fill="#fff" d="M3.5 1.5l2.5 0 1 3.5-1.6 1.2a8 8 0 0 0 4.4 4.4L11 9l3.5 1v2.5c0 1-1 2-2 2C6.4 14.5 1.5 9.6 1.5 3.5c0-1 1-2 2-2z"/></svg>
      0208 794 2160
    </p>
    <p class="contact__row">
      <svg viewBox="0 0 16 16" aria-hidden="true"><rect x="1.5" y="3.5" width="13" height="9" rx="1" fill="none" stroke="#fff" stroke-width="1.5"/><path d="M1.5 4l6.5 5 6.5-5" fill="none" stroke="#fff" stroke-width="1.5"/></svg>
      info@penningtondoweaesthetics.co.uk
    </p>
    <p class="contact__row">
      <svg viewBox="0 0 16 16" aria-hidden="true"><circle cx="8" cy="8" r="6.5" fill="none" stroke="#fff" stroke-width="1.5"/><path d="M1.5 8h13M8 1.5c-3 3.5-3 9.5 0 13M8 1.5c3 3.5 3 9.5 0 13" fill="none" stroke="#fff" stroke-width="1.2"/></svg>
      www.penningtondoweaesthetics.co.uk
    </p>
    <p class="contact__address">
      52 Farrowmere Road<br>
      4 Brackwell High Street<br>
      KT9 4WQ
    </p>
  </div>
  <p class="wordmark-vertical">
    <span class="line1">Pennington Dowe</span>
    <span class="line2">Aesthetics</span>
  </p>
</section>

</body>
</html>
```